Caltrisa Website Design

Caltrisa Solutions. http://caltrisasolutions-example.com is looking to redesign our current website with a modern feel and added functionality.

The winning design will be coded in HTML 5 and be responsive built for mobile. You can use bootstrap, jquery.

Wordpress or wix will not be accepted.

Page 1
http://caltrisasolutions-example.com/

Page 2
http://caltrisasolutions-example.com/who_we_are.php

Page 3
http://caltrisasolutions-example.com/solutions_offered.php

Page 4
http://caltrisasolutions-example.com/faq.php

Here are some pages from our competitors. Please see notes of our likes and dislikes of each page.

https://www.pellorcare-example.com/

Likes: Ability to explore opportunities / “Neighbour Threads” Highlighting involvement in the community.

Dislike: Layout not very interactive. Feels clunky

https://www.vantrelmed-example.com/

Likes: Visually appealing. Using nice images.

Dislike: Not very intuitive. You need to read a bit to figure out what they do and what they’re about.. Not overly interactive either.

https://kribowork-example.com/

Likes: Clean, Using a puppy as part of marketing, highlights Stability and Quality

Dislikes: All services offered are further down and requires you click and drill down to get info

https://www.sundrilex-example.com/

Likes: Has video about Improving Coding Accuracy which is important to clients. Their “Our Solutions” Section is clear and not too wordy. Once you click on Learn More it provides good info.

Dislikes: Not as visually appealing. No wow factor. Seems a bit basic.

https://fenmorpa-example.com/

Likes: Section that allows clients to request facility analysis. Has easy to find menu dropdowns at the top of page.

Dislikes: Boring site. Nothing special at all.

https://quillbrook-example.com/

Likes: I actually like this site overall

Dislikes: It is a little busy, but other than that it’s pretty nice.

https://tazurn-example.com

Likes: although their choice of doodle graphics is overly busy, I like that it’s different from every other vendor. To me, it stands out. I also like how when you scroll, it pops up a new highlight and keeps the watermark in the background.

Dislikes: Choice of font is a lil hard to read and not easy on the eyes. I believe the bold and color of the font make it appear too busy.

https://wexlingford-example.com/

Likes: Probably my favorite. Very professional and interactive. I like how it scrolls through images at the top with links to allow you to dive in further. I also like the interactive photo blocks towards the bottom and how they use photos from past speaking events that give them credibility and highlight Dr Wexlingford speaking.

Dislikes: Nothing specific

Do to the ongoing Corona Virus here in Florida we have been dealing with that. Most will be working from home this week and plan to focus on finalizing this project. Thanks

Please extend this. With the current COVID19 stuff this is kind of been put on the back burner.

```html
<!DOCTYPE html>
<html lang="en">
<head>
<meta charset="utf-8">
<title>Caltrisa Solutions</title>
<link rel="stylesheet" href="https://fonts.googleapis.com/css2?family=Open+Sans:wght@400;600;700&display=swap">
<style>
:root{
  --navy:#2e3192;
  --navy-deep:#15166a;
  --navy-text:#1d1f6e;
  --green:#55a85a;
  --green-soft:#7cbf7f;
  --lilac:#a8a7f2;
  --light:#f3f3f5;
  --white:#ffffff;
  --text:#333344;
  --muted:#c9c9e6;
}
*{box-sizing:border-box;margin:0;padding:0}
html,body{width:1200px;height:4062px;overflow:hidden}
body{font-family:"Open Sans",Arial,sans-serif;color:var(--text);background:var(--white);position:relative}
.section{position:absolute;left:0;width:1200px}
.abs{position:absolute}
.btn{position:absolute;display:flex;align-items:center;justify-content:center;font-size:13px;font-weight:700;letter-spacing:.3px;text-transform:uppercase}
.btn-navy{background:var(--navy);color:var(--white)}
.btn-green{background:var(--green-soft);color:var(--navy-text)}
.center{text-align:center}

/* top bar */
.topbar{top:0;height:50px;background:var(--navy);color:var(--white);font-size:13px}
.topbar .addr{left:156px;top:16px;display:flex;gap:6px;align-items:center}
.topbar .phone{left:693px;top:16px;display:flex;gap:6px;align-items:center}
.social{display:flex;gap:10px}
.social span{width:27px;height:27px;border:1.5px solid var(--white);border-radius:50%;display:block}
.topbar .social{position:absolute;left:831px;top:11px}
.topbar .cta{left:922px;top:6px;width:120px;height:36px;background:var(--white);color:var(--navy-text);font-size:12px}

/* header */
.header{top:50px;height:71px;background:var(--white)}
.brand{left:156px;top:18px;font-size:30px;font-weight:700;color:var(--green);letter-spacing:.5px}
.nav{right:158px;top:24px;display:flex;gap:26px;font-size:13.5px;color:var(--navy-text);align-items:center}
.nav .active{color:var(--navy);border-bottom:3px solid var(--green);padding-bottom:6px;margin-top:9px}

/* hero */
.hero{top:121px;height:494px;background:linear-gradient(90deg,#f7f7f9 0%,#f1f1f3 45%,#e8e6e6 100%)}
.hero-photo{left:520px;top:0;width:680px;height:494px;background:linear-gradient(100deg,rgba(241,241,243,0) 0%,#ded9d6 25%,#cfc3bb 55%,#a7968b 80%,#ece6e1 100%)}
.hero h2{left:156px;top:110px;font-size:43px;font-weight:400;color:var(--navy-text);line-height:1}
.hero h2 b{font-weight:700}
.hero h1{left:154px;top:156px;font-size:57px;font-weight:700;color:#3b8a3f;line-height:1.1}
.hero p{left:156px;top:230px;width:360px;font-size:16px;line-height:21px;color:#222}
.hero .btn{left:156px;top:317px;width:128px;height:34px}
.dots{left:156px;top:440px;display:flex;gap:7px}
.dots i{width:7px;height:7px;border-radius:50%;border:1px solid var(--green);display:block}
.dots i:first-child{background:var(--navy);border-color:var(--navy)}

/* search */
.search{top:615px;height:408px;background:var(--navy-deep);color:var(--white)}
.search .divider{left:599px;top:60px;width:1px;height:280px;background:rgba(255,255,255,.25)}
.form-col{position:absolute;top:68px;width:348px}
.form-col h3{font-size:24px;font-weight:600;margin-bottom:10px}
.form-col label{display:block;font-size:12.5px;color:var(--muted);margin:4px 0 6px 4px}
.field{height:44px;background:var(--white);color:#333;font-size:12.5px;display:flex;align-items:center;justify-content:space-between;padding:0 12px;margin-bottom:14px}
.row{display:flex;gap:8px}
.row .field{width:284px}
.send{width:52px;height:46px;background:var(--green-soft);display:flex;align-items:center;justify-content:center}

/* why */
.why{top:1023px;height:578px;background:var(--light)}
.section-title{position:absolute;left:0;width:1200px;text-align:center;font-weight:600;color:var(--navy-text)}
.why .section-title{top:78px;font-size:36px}
.feature{position:absolute;top:156px;width:280px;text-align:center}
.feature .disc{width:190px;height:190px;border-radius:50%;margin:0 auto 20px;border:5px solid var(--navy);background:var(--lilac);display:flex;align-items:center;justify-content:center}
.feature .disc.alt{border-color:var(--green);background:var(--green-soft)}
.feature h4{font-size:19px;font-weight:600;line-height:25px;color:var(--navy);text-transform:uppercase;margin-bottom:8px}
.feature h4.alt{color:var(--green)}
.feature p{font-size:14px;line-height:19px;color:#444}

/* about */
.about{top:1601px;height:501px;background:var(--white)}
.about h2{left:157px;top:53px;font-size:41px;font-weight:600;color:var(--navy-text)}
.about .copy{left:158px;top:111px;width:430px;font-size:14px;line-height:19px;color:#333}
.about .copy p{margin-bottom:19px}
.about .btn{left:158px;top:408px;width:126px;height:35px}
.video{left:607px;top:96px;width:439px;height:313px;border:4px solid var(--white);box-shadow:0 3px 12px rgba(0,0,0,.35);background:linear-gradient(120deg,#8a5a44 0%,#b98a70 35%,#d9cfc8 60%,#5b6a86 100%)}
.play{left:190px;top:127px;width:52px;height:52px;border-radius:50%;background:var(--white);display:flex;align-items:center;justify-content:center}

/* solution */
.solution{top:2102px;height:623px;background:var(--light)}
.solution .section-title{top:72px;font-size:37px}
.sol{position:absolute;top:150px;width:290px;text-align:center}
.hex{width:213px;height:186px;margin:0 auto 24px;clip-path:polygon(25% 0,75% 0,100% 50%,75% 100%,25% 100%,0 50%);background:var(--white);display:flex;align-items:center;justify-content:center}
.hex div{width:203px;height:176px;clip-path:polygon(25% 0,75% 0,100% 50%,75% 100%,25% 100%,0 50%)}
.sol h4{font-size:19.5px;font-weight:600;line-height:25px;color:var(--navy);margin-bottom:20px;min-height:75px}
.sol p{font-size:14px;line-height:19px;color:#444;height:58px}
.sol .btn{position:relative;margin:14px auto 0;width:126px;height:35px}

/* get started */
.started{top:2725px;height:385px;background:var(--green);color:var(--white)}
.started .section-title{top:102px;font-size:38px;color:var(--white)}
.started p{position:absolute;left:230px;width:740px;top:164px;text-align:center;font-size:14px;line-height:21px}
.started .btn{left:538px;top:238px;width:124px;height:37px;background:var(--white);color:var(--navy)}

/* opportunities */
.opps{top:3110px;height:307px;background:var(--light)}
.opps .section-title{top:100px;font-size:34px}
.opps .btn{left:539px;top:162px;width:124px;height:35px}

/* footer */
.footer{top:3417px;height:379px;background:var(--navy-deep);color:var(--white)}
.footer h5{position:absolute;top:68px;font-size:15px;font-weight:600;letter-spacing:.3px}
.map{left:158px;top:109px;width:359px;height:215px;background:linear-gradient(135deg,#eef1f4 0%,#dfe9f2 50%,#f3eed6 100%)}
.contact-list{left:553px;top:105px;width:260px;font-size:13px;line-height:18px}
.contact-list li{list-style:none;display:flex;gap:14px;align-items:center;margin-bottom:16px}
.contact-list .ico{width:30px;height:30px;border:1.5px solid var(--white);border-radius:50%;flex:none;display:flex;align-items:center;justify-content:center}
.touch{left:833px;top:109px;width:210px}
.touch .in{height:30px;background:#efeff1;color:#333;font-size:11px;padding:8px 8px;margin-bottom:8px}
.touch .msg{height:59px}
.touch .btn{position:relative;width:126px;height:35px;background:var(--green-soft);color:var(--navy-text);margin-top:3px}

.bottom{top:3796px;height:266px;background:var(--navy-deep);color:var(--white);border-top:1px solid rgba(255,255,255,.18)}
.bottom .brand-foot{left:0;width:1200px;top:30px;text-align:center;font-size:34px;font-weight:700;letter-spacing:.5px}
.bottom .rule{left:0;top:95px;width:1200px;height:1px;background:rgba(255,255,255,.18)}
.bottom .social{position:absolute;left:560px;top:105px;gap:12px}
.bottom .social span{width:35px;height:35px}
.links{left:0;width:1200px;top:143px;text-align:center;font-size:13px}
.links span{margin:0 16px}
.copyright{left:0;width:1200px;top:194px;text-align:center;font-size:13px}
</style>
</head>
<body>

<div class="section topbar">
  <div class="abs addr">
    <svg width="10" height="13" viewBox="0 0 10 13"><path d="M5 0a5 5 0 0 0-5 5c0 3.5 5 8 5 8s5-4.5 5-8a5 5 0 0 0-5-5zm0 7a2 2 0 1 1 0-4 2 2 0 0 1 0 4z" fill="#fff"/></svg>
    4470 Harbor Crest Blvd Suite 118, Palm Coast, FL 32137
  </div>
  <div class="abs phone">
    <svg width="11" height="11" viewBox="0 0 24 24"><path d="M6.6 10.8a15 15 0 0 0 6.6 6.6l2.2-2.2a1 1 0 0 1 1-.25 11 11 0 0 0 3.6.6 1 1 0 0 1 1 1V20a1 1 0 0 1-1 1A17 17 0 0 1 3 4a1 1 0 0 1 1-1h3.5a1 1 0 0 1 1 1 11 11 0 0 0 .6 3.6 1 1 0 0 1-.25 1z" fill="#fff"/></svg>
    (866) 555-0147
  </div>
  <div class="social"><span></span><span></span></div>
  <div class="btn cta">Contact Us</div>
</div>

<div class="section header">
  <div class="abs brand">Caltrisa</div>
  <nav class="abs nav">
    <span class="active">HOME</span>
    <span>ABOUT CALTRISA SOLUTIONS ⌄</span>
    <span>QUALITY BOARD</span>
    <svg width="13" height="13" viewBox="0 0 24 24"><circle cx="10" cy="10" r="7" fill="none" stroke="#1d1f6e" stroke-width="3"/><path d="M15 15l7 7" stroke="#1d1f6e" stroke-width="3"/></svg>
  </nav>
</div>

<div class="section hero">
  <div class="abs hero-photo" role="img" aria-label="Photo of a doctor at a desk consulting with a patient"></div>
  <h2 class="abs">REVENUE <b>CYCLE</b></h2>
  <h1 class="abs">Optimization</h1>
  <p class="abs">Caltrisa Solutions was founded with one reason in mind, applying the true concept of world-class customer service ...</p>
  <div class="btn btn-green">Apply Now</div>
  <div class="abs dots"><i></i><i></i><i></i></div>
</div>

<div class="section search">
  <div class="abs divider"></div>
  <div class="form-col" style="left:185px">
    <h3>Search Career Opportunities</h3>
    <label>What are your staffing needs?</label>
    <div class="field">Select Profession <span>⌄</span></div>
    <label>Different Backgrounds</label>
    <div class="field">Travel Or Remote <span>⌄</span></div>
    <label>Location</label>
    <div class="row"><div class="field">Select State <span>⌄</span></div><div class="send"><svg width="16" height="16" viewBox="0 0 24 24"><path d="M22 2L2 10l8 3 3 8z" fill="#1d1f6e"/></svg></div></div>
  </div>
  <div class="form-col" style="left:656px">
    <h3>Quickly Speak With A Recruiter</h3>
    <label>Enter Your Name</label>
    <div class="field">Name</div>
    <label>Enter your Email</label>
    <div class="field">Mail</div>
    <label>Location</label>
    <div class="row"><div class="field">Select State <span>⌄</span></div><div class="send"><svg width="16" height="16" viewBox="0 0 24 24"><path d="M22 2L2 10l8 3 3 8z" fill="#1d1f6e"/></svg></div></div>
  </div>
</div>

<div class="section why">
  <h2 class="section-title">WHY CHOOSE US</h2>
  <div class="feature" style="left:166px">
    <div class="disc" role="img" aria-label="Icon of a hand offering benefits"></div>
    <h4>Employer Paid<br>Benefits</h4>
    <p>Caltrisa Solutions covers all medical benefits for employees. We offer a wide-array of health insurance options to suit your every need.</p>
  </div>
  <div class="feature" style="left:464px">
    <div class="disc alt" role="img" aria-label="Icon of documents and a briefcase"></div>
    <h4 class="alt">Salaried<br>Employment</h4>
    <p>Caltrisa offers both salaried and hourly employment models. Salaried consultants are allotted up to 4 weeks of paid bench time.</p>
  </div>
  <div class="feature" style="left:762px">
    <div class="disc" role="img" aria-label="Icon of a document under a magnifying glass"></div>
    <h4>Evaluate What's<br>Important</h4>
    <p>Caltrisa is dedicated to work-life balance. That is why we offer paid holidays, paid vacation/sick time, education benefits, our annual Balance bonus, amongst other</p>
  </div>
</div>

<div class="section about">
  <h2 class="abs">ABOUT US</h2>
  <div class="abs copy">
    <p>Caltrisa Solutions was founded with one reason in mind, applying the true concept of world-class customer service to our consultant and client relationships.</p>
    <p>Our goal is to identify consultants with a comprehensive and diverse background that have a passion to be a part of something more. Caltrisa Solutions is keen on listening to our consultants' interests and what's important to them, by taking an interest in their lifestyle, family life, and surrounding community. From there, we can begin to identify the type of environment that suits our consultants' expertise. We are enthusiastic about bringing our culture to today's world of healthcare consulting. It is time to be excited about a company that works for you.</p>
  </div>
  <div class="btn btn-navy">Read More</div>
  <div class="abs video" role="img" aria-label="Video still of a doctor speaking with an older couple at home">
    <div class="abs play"><svg width="18" height="20" viewBox="0 0 18 20"><path d="M2 1l15 9-15 9z" fill="#e02424"/></svg></div>
  </div>
</div>

<div class="section solution">
  <h2 class="section-title">OUR SOLUTION</h2>
  <div class="sol" style="left:155px">
    <div class="hex"><div role="img" aria-label="Photo of a team meeting around a table" style="background:linear-gradient(135deg,#e9e9ea,#9aa0a8 55%,#3c3f48)"></div></div>
    <h4>REVENUE CYCLE<br>OPTIMIZATION (RCO)</h4>
    <p>RCO improves patient outcomes by applying Caltrisa Solutions' staff augmentation approach</p>
    <div class="btn btn-navy">Read More</div>
  </div>
  <div class="sol" style="left:455px">
    <div class="hex"><div role="img" aria-label="Photo of a group of medical staff" style="background:linear-gradient(135deg,#6b7ea0,#c7c6cc 50%,#2c3558)"></div></div>
    <h4>CLINICAL DOCUMENTATION IMPROVEMENT SOLUTIONS (CDIS)</h4>
    <p>Caltrisa Solutions brings over 15 years of CDI staff augmentation experience to our clients . . .</p>
    <div class="btn btn-navy">Read More</div>
  </div>
  <div class="sol" style="left:754px">
    <div class="hex"><div role="img" aria-label="Photo of a diagnosis form with a pen" style="background:linear-gradient(135deg,#dcdcdc,#f4f4f4 50%,#8d8f95)"></div></div>
    <h4>EVALUATE WHAT'S<br>IMPORTANT</h4>
    <p>Caltrisa Solutions evaluates the types of consultants that can successfully support a client based . . .</p>
    <div class="btn btn-navy">Read More</div>
  </div>
</div>

<div class="section started">
  <h2 class="section-title">GET STARTED TODAY</h2>
  <p>We're always looking for exceptional consultants to join our team – consultants who love their job and love working for a company who puts their needs first. If you're interested in pursing a career with Caltrisa Solutions, we'd love to speak with you today.</p>
  <div class="btn">Apply Now</div>
</div>

<div class="section opps">
  <h2 class="section-title">OPPORTUNITIES AVAILABLE IN MIAMI,FL</h2>
  <div class="btn btn-navy">Contact Us</div>
</div>

<div class="section footer">
  <h5 style="left:158px">LOCATION</h5>
  <div class="abs map" role="img" aria-label="Street map showing the office location"></div>
  <h5 style="left:553px">CONTACT US</h5>
  <ul class="abs contact-list">
    <li><span class="ico"><svg width="10" height="13" viewBox="0 0 10 13"><path d="M5 0a5 5 0 0 0-5 5c0 3.5 5 8 5 8s5-4.5 5-8a5 5 0 0 0-5-5zm0 7a2 2 0 1 1 0-4 2 2 0 0 1 0 4z" fill="#fff"/></svg></span><span>4470 Harbor Crest Blvd Suite 118<br>Palm Coast, FL 32137</span></li>
    <li><span class="ico"><svg width="12" height="12" viewBox="0 0 24 24"><path d="M6.6 10.8a15 15 0 0 0 6.6 6.6l2.2-2.2a1 1 0 0 1 1-.25 11 11 0 0 0 3.6.6 1 1 0 0 1 1 1V20a1 1 0 0 1-1 1A17 17 0 0 1 3 4a1 1 0 0 1 1-1h3.5a1 1 0 0 1 1 1 11 11 0 0 0 .6 3.6 1 1 0 0 1-.25 1z" fill="#fff"/></svg></span><span>(866) 555-0147</span></li>
    <li><span class="ico"><svg width="13" height="10" viewBox="0 0 13 10"><rect x=".5" y=".5" width="12" height="9" fill="none" stroke="#fff"/><path d="M.5.5l6 5 6-5" fill="none" stroke="#fff"/></svg></span><span>jobs@caltrisasolutions-example.com</span></li>
  </ul>
  <h5 style="left:833px">GET IN TOUCH</h5>
  <div class="abs touch">
    <div class="in">Name :</div>
    <div class="in">Email :</div>
    <div class="in">Ph No :</div>
    <div class="in msg">Message :</div>
    <div class="btn">Send Now</div>
  </div>
</div>

<div class="section bottom">
  <div class="abs brand-foot">Caltrisa</div>
  <div class="abs rule"></div>
  <div class="social"><span></span><span></span></div>
  <div class="abs links">Home <span>I</span> About Caltrisa Solutions <span>I</span> QUALITY BOARD</div>
  <div class="abs copyright">Copyright©2020 Caltrisa solutions. All Rights Reserved.</div>
</div>

</body>
</html>
```